Business Card design for shipping company 'FARNHOLT MARITIME LTD'

Classic / traditional business card in black Garamond / Times New Roman or similar text for a shipping / marine transport company, containing the following information:

QUOTE

FARNHOLT MARITIME LTD

PETER CALLOWAY FICS

T: +44 7923 615087
E: vessels@farnholt-mar.com

UNQUOTE

Target Market(s)

Marine / Shipping industry

Contact Information for Business Card

FARNHOLT MARITIME LTD PETER CALLOWAY FICS T: +44 7923 615087 E: vessels@farnholt-mar.com

Font styles to use
Serif

Colors

Designer to choose colors to be used in the design.

Requirements
Must have
• Garamond / Times New Roman or similar text in black colour

```html
<!DOCTYPE html>
<html lang="en">
<head>
<meta charset="utf-8">
<title>Farnholt Maritime Ltd – Business Card</title>
<link rel="stylesheet" href="https://fonts.googleapis.com/css2?family=EB+Garamond:ital,wght@0,500;0,700;1,500&display=swap">
<style>
  :root {
    --backdrop: #e9e4dc;
    --card-dark: #000000;
    --card-light: #ffffff;
    --brand-red: #e3141b;
    --ink: #111111;
    --map-grey-1: #3a3a3a;
    --map-grey-2: #1a1a1a;
  }
  * { margin: 0; padding: 0; box-sizing: border-box; }
  html, body {
    width: 1200px; height: 675px; overflow: hidden;
    background: var(--backdrop);
    font-family: "EB Garamond", "Times New Roman", serif;
  }
  .stage {
    width: 1200px; height: 675px;
    display: flex; align-items: center; justify-content: center; gap: 60px;
  }
  .card {
    position: relative;
    width: 520px; height: 298px;
    box-shadow: 0 10px 28px rgba(0,0,0,0.25);
    overflow: hidden;
  }
  .card--front { background: var(--card-dark); }
  .card--back { background: var(--card-light); }

  .world-map-area {
    position: absolute; left: 70px; top: 40px; width: 390px; height: 220px;
    border-radius: 40% 45% 40% 50%;
    background: radial-gradient(ellipse at 55% 40%, var(--map-grey-1), var(--map-grey-2) 60%, transparent 78%);
    opacity: 0.9;
  }
  .front-company {
    position: absolute; left: 0; right: 0; top: 50%;
    transform: translateY(-50%);
    text-align: center;
    color: var(--brand-red);
    font-weight: 700; font-size: 33px; letter-spacing: 0.5px;
  }

  .back-company {
    position: absolute; left: 0; right: 0; top: 46px;
    text-align: center;
    color: var(--brand-red);
    font-weight: 700; font-size: 30px; letter-spacing: 0.5px;
  }
  .person {
    position: absolute; left: 0; right: 0; top: 112px;
    text-align: center; color: var(--ink);
  }
  .person-name { font-weight: 700; font-size: 30px; line-height: 1; }
  .person-title { font-style: italic; font-size: 11px; margin-top: 2px; margin-left: 70px; }
  .divider {
    position: absolute; left: 110px; right: 60px; top: 178px;
    height: 1px; background: var(--brand-red);
  }
  .contacts {
    position: absolute; left: 150px; top: 194px;
    list-style: none; color: var(--ink);
    font-weight: 700; font-size: 15px;
  }
  .contact-item { display: flex; align-items: center; gap: 8px; height: 30px; }
  .contact-icon { width: 17px; height: 17px; flex: none; }
</style>
</head>
<body>
<main class="stage">
  <section class="card card--front">
    <div class="world-map-area" role="img" aria-label="Faint world map illustration"></div>
    <h1 class="front-company">FARNHOLT MARITIME LTD</h1>
  </section>

  <section class="card card--back">
    <h2 class="back-company">FARNHOLT MARITIME LTD</h2>
    <div class="person">
      <p class="person-name">Peter Calloway</p>
      <p class="person-title">FICS</p>
    </div>
    <div class="divider"></div>
    <ul class="contacts">
      <li class="contact-item">
        <svg class="contact-icon" viewBox="0 0 20 20" aria-hidden="true">
          <circle cx="10" cy="10" r="9" fill="none" stroke="var(--brand-red)" stroke-width="1.5"/>
          <path d="M6.5 6c1-.8 1.6-.6 2 .3l.6 1.3c.2.5 0 .9-.4 1.2-.3.2-.3.5-.1.8.6 1 1.2 1.6 2.2 2.2.3.2.6.2.8-.1.3-.4.7-.6 1.2-.4l1.3.6c.9.4 1.1 1 .3 2-1 1.1-3 .9-5.2-1.3S5.4 7 6.5 6z" fill="var(--brand-red)"/>
        </svg>
        <span>+44 7923 615087</span>
      </li>
      <li class="contact-item">
        <svg class="contact-icon" viewBox="0 0 20 20" aria-hidden="true">
          <circle cx="10" cy="10" r="9" fill="none" stroke="var(--brand-red)" stroke-width="1.5"/>
          <rect x="5" y="6.5" width="10" height="7" fill="var(--brand-red)"/>
          <path d="M5 6.5l5 4 5-4" fill="none" stroke="#fff" stroke-width="1"/>
        </svg>
        <span>vessels@farnholt-mar.com</span>
      </li>
    </ul>
  </section>
</main>
</body>
</html>
```